Design new Brackwater Asset business card 2016

We need a new business card for our company Brackwater Asset Partners. We are a niche Alternative Investment Fund Manager based in Chester, in the North West of the UK.We market our services to global institutions such as banks, insurance companies, pension funds, etc. as well as wealthy individuals. Our main markets are Europe (Germany\France\Switzerland), the US and parts of Asia.
The design needs to be in line with existing company branding. Life the assets we deal with, the business card might suggest, "niche\alternative" type of attributes - however, it needs to remain professional, clean and appropriate for our client base.
Our existing business card format with relevant factual information is included, along with logo and branding details.

Target Market(s)

We market our services to global institutions such as banks, insurance companies, pension funds, etc. as well as wealthy individuals.

Industry/Entity Type

Financial Service

Contact Information for Business Card

please see attached pdf for information on existing business card which we should aim to convey on your new design. However:
- the wording "Brackwater Asset Partners Ltd is Authorised and Regulated
by the Monetary Oversight Bureau. Registered No. 7139046" should be replaced with , "Brackwater Asset Partners Ltd is an Alternative Investment Fund Manager Authorised and Regulated by the Monetary Oversight Bureau. Registered No. 7139046"
- the "reception" word on reverse can be omitted.
- the "retail: www.toplivanex.co.uk" wording can be omitted.
- the QR code is not required in the new version.

Font styles to use
Serif
Sans Serif

Requirements
Must have
• information on current business card, subject to comments provided above.
Nice to have
• Use of areas of solid colour instead of large areas of white space might be nice to experiment with. However, still need to have the general look and feel of the brand as presented on our website www.bwfundco.co.uk
• If we had space for 3 bullet points describing what we do\who we are, this might be good to try out. e.g. alternative investment fund manager, longevity specialist, founded 1990.
• Also, we have a new tag line, "expertise with longevity" which might fit nicely somewhere on the business card.
Should not have
• - no QR code
• - should not use all the colours in our logo as it looks very garish! Using one or two colours with black\white etc, seems to work better.

```html
<!DOCTYPE html>
<html lang="en">
<head>
<meta charset="utf-8">
<title>Brackwater Asset Partners – Business Card</title>
<link rel="stylesheet" href="https://fonts.googleapis.com/css2?family=Noto+Serif:ital,wght@0,400;0,700;1,400&family=Roboto+Slab:wght@500&family=Open+Sans:wght@400&display=swap">
<style>
  :root {
    --backdrop: #e4e4e2;
    --card-paper: #f4f4f2;
    --olive: #8d8603;
    --olive-text: #8a8200;
    --brown: #5b3311;
    --ink: #3c3c3c;
    --white: #ffffff;
  }
  * { box-sizing: border-box; margin: 0; padding: 0; }
  html, body {
    width: 1105px; height: 1200px; overflow: hidden;
    background: var(--backdrop);
  }
  .card {
    position: absolute; left: 180px; width: 746px; height: 427px;
    overflow: hidden;
  }
  /* ---------- Front ---------- */
  .card--front { top: 120px; background: var(--card-paper); }
  .brand {
    position: absolute; right: 42px; top: 22px;
    display: flex; flex-direction: column; align-items: center; gap: 18px;
  }
  .brand__mark {
    width: 116px; height: 116px; border-radius: 50%;
    background: var(--olive);
  }
  .brand__name {
    font-family: "Noto Serif", serif; font-weight: 400;
    font-size: 29px; color: var(--olive-text); white-space: nowrap;
  }
  .person { position: absolute; left: 33px; top: 228px; right: 42px; }
  .person__name {
    font-family: "Roboto Slab", serif; font-weight: 500;
    font-size: 27px; color: var(--brown); line-height: 1.2;
  }
  .person__role {
    display: flex; align-items: center; gap: 4px;
    font-family: "Open Sans", sans-serif; font-size: 19px; color: var(--olive-text);
    margin-top: 2px;
  }
  .person__role::after {
    content: ""; flex: 1; height: 1px; background: var(--olive); margin-top: 6px;
  }
  .contact {
    position: absolute; top: 303px;
    font-family: "Noto Serif", serif; font-size: 19px; color: var(--ink);
    list-style: none; line-height: 29px;
  }
  .contact li { display: flex; align-items: center; gap: 10px; }
  .contact--phones { left: 33px; }
  .contact--online { right: 42px; }
  .contact--online li { justify-content: flex-end; }
  .contact svg { width: 18px; height: 18px; fill: var(--ink); flex: none; }
  .contact--online svg { order: 2; }
  .base-band {
    position: absolute; left: 0; right: 0; bottom: 0; height: 16px; background: var(--brown);
  }
  .tagline {
    position: absolute; right: 0; bottom: 0; width: 322px; height: 44px;
    background: var(--olive);
    clip-path: polygon(32px 0, 100% 0, 100% 100%, 0 100%);
    border-left: 0;
    display: flex; align-items: center; justify-content: flex-end; padding-right: 22px;
    font-family: "Noto Serif", serif; font-weight: 700; font-size: 20px; color: var(--white);
  }
  .tagline-edge {
    position: absolute; right: 322px; bottom: 0; width: 36px; height: 44px;
  }
  /* ---------- Back ---------- */
  .card--back { top: 636px; background: var(--olive); color: var(--white); text-align: center; }
  .back-brand {
    position: absolute; left: 0; right: 0; top: 52px;
    display: flex; flex-direction: column; align-items: center; gap: 20px;
  }
  .back-brand .brand__mark { background: var(--white); width: 120px; height: 120px; }
  .back-brand .brand__name { color: var(--white); font-size: 33px; }
  .services {
    position: absolute; left: 0; right: 0; top: 307px;
    font-family: "Noto Serif", serif; font-size: 20px;
  }
  .divider {
    position: absolute; left: 150px; right: 150px; top: 342px; height: 1px;
    background: rgba(255,255,255,0.55);
  }
  .legal {
    position: absolute; left: 0; right: 0; top: 350px;
    font-family: "Noto Serif", serif; font-style: italic; font-size: 15.5px; line-height: 24px;
  }
</style>
</head>
<body>

<section class="card card--front">
  <div class="brand">
    <span class="brand__mark" aria-hidden="true"></span>
    <span class="brand__name">Brackwater Asset Partners</span>
  </div>

  <div class="person">
    <p class="person__name">Martin Hale</p>
    <p class="person__role">Non-Executive Chairman</p>
  </div>

  <ul class="contact contact--phones">
    <li>
      <svg viewBox="0 0 24 24" aria-hidden="true"><path d="M6.6 10.8a15.1 15.1 0 0 0 6.6 6.6l2.2-2.2a1 1 0 0 1 1-.25 11.4 11.4 0 0 0 3.6.57 1 1 0 0 1 1 1V20a1 1 0 0 1-1 1A17 17 0 0 1 3 4a1 1 0 0 1 1-1h3.5a1 1 0 0 1 1 1c0 1.25.2 2.45.57 3.57a1 1 0 0 1-.25 1z"/></svg>
      +44 (0)1632 960418
    </li>
    <li>
      <svg viewBox="0 0 24 24" aria-hidden="true"><path d="M7 1h10a2 2 0 0 1 2 2v18a2 2 0 0 1-2 2H7a2 2 0 0 1-2-2V3a2 2 0 0 1 2-2zm0 3v14h10V4zm5 15.2a1.2 1.2 0 1 0 0 2.4 1.2 1.2 0 0 0 0-2.4z"/></svg>
      +44 (0)7700 900562
    </li>
  </ul>

  <ul class="contact contact--online">
    <li>
      <svg viewBox="0 0 24 24" aria-hidden="true"><path d="M2 5h20v14H2zm2 2v.5l8 5 8-5V7zm0 2.9V17h16V9.9l-8 5z"/></svg>
      mhale@bwfundco.co.uk
    </li>
    <li>
      <svg viewBox="0 0 24 24" aria-hidden="true"><path d="M12 2a10 10 0 1 0 0 20 10 10 0 0 0 0-20zm-1 17.9A8 8 0 0 1 4.1 10L9 15v1a2 2 0 0 0 2 2zm6.9-2.5A2 2 0 0 0 16 16h-1v-3a1 1 0 0 0-1-1H8v-2h2a1 1 0 0 0 1-1V7h2a2 2 0 0 0 2-2v-.4a8 8 0 0 1 2.9 12.8z"/></svg>
      www.bwfundco.co.uk
    </li>
  </ul>

  <div class="base-band"></div>
  <p class="tagline">Expertise with longevity</p>
</section>

<section class="card card--back">
  <div class="back-brand">
    <span class="brand__mark" aria-hidden="true"></span>
    <span class="brand__name">Brackwater Asset Partners</span>
  </div>
  <p class="services">Alternative Investment Fund Manager • Longevity Specialist • Founded 1990</p>
  <div class="divider"></div>
  <p class="legal">Brackwater Asset Partners Ltd is an Alternative Investment Fund Manager Authorised<br>and Regulated by the Monetary Oversight Bureau. Registered No. 7139046</p>
</section>

</body>
</html>
```